4th Generation Family Business Needs a New Card Design!

We are a family owned 4th Generation company. We are based in the Sydney, Australia area and we are desperately in need of a more modern and classy card. We are monumental masons who design, supply & erect lasting memorials throughout cemeteries in Sydney. Our customers are normally in a period of grieving. I have attached logo files that will need to be implemented on the card. Company was established 1935. Australian Owned and Operated. Card needs to be designed to PRINTLY.com specification.

Target Market(s)

Our target market is based upon people that a grieving for family members that have passed away. We also deal with alot of companies that own and operate cemeteries.

Industry/Entity Type

Business

Contact Information for Business Card

Oliver Brantley, Operations Manager, 0417552908, oliver@hollowaystoneworks.com.au
Martin Brantley, Director, 0431906627, martin@hollowaystoneworks.com.au
Phone # 02 9634 2258
Website: www.hollowaystoneworks.com.au
Address: Suite 17, 8 Calloway Lane, East Penrose, Sydney NSW 2290

Font styles to use
Serif
Decorative
Script

Requirements
Must have
• Would like to see the logo nicely implemented with a modern design. Embossed lettering would be a nice additive.

```html
<!DOCTYPE html>
<html lang="en">
<head>
<meta charset="utf-8">
<title>Holloway Stoneworks – Business Card</title>
<link href="https://fonts.googleapis.com/css2?family=Cinzel:wght@600&family=Montserrat:wght@400;600;700&display=swap" rel="stylesheet">
<style>
  :root {
    --gold: #efc12f;
    --ink: #0b0b0b;
    --paper: #ffffff;
    --backdrop: #2e2e30;
    --muted: #d9d9d9;
  }
  * { box-sizing: border-box; margin: 0; padding: 0; }
  html, body { width: 1200px; height: 900px; overflow: hidden; }
  body {
    background: var(--backdrop);
    font-family: "Montserrat", Arial, sans-serif;
    position: relative;
  }
  .card {
    position: absolute;
    left: 320px;
    width: 560px;
    height: 320px;
    border-radius: 22px;
    overflow: hidden;
    box-shadow: 0 14px 30px rgba(0,0,0,0.45);
  }
  /* Front */
  .card-front { top: 100px; background: var(--gold); }
  .front-brand {
    position: absolute; left: 0; right: 0; top: 105px;
    text-align: center;
  }
  .brand-name {
    font-family: "Cinzel", Georgia, serif;
    font-weight: 600;
    color: var(--ink);
    letter-spacing: 2px;
    line-height: 1.05;
  }
  .front-brand .brand-name { font-size: 40px; }
  .front-brand .brand-rule {
    width: 300px; height: 2px; background: var(--paper);
    margin: 14px auto 0;
  }
  .front-web {
    position: absolute; left: 0; right: 0; bottom: 48px;
    text-align: center; color: var(--paper); font-size: 15px;
  }
  .front-web strong { font-weight: 700; }

  /* Back */
  .card-back { top: 480px; background: var(--ink); }
  .back-top {
    position: absolute; left: 0; top: 0; width: 100%; height: 140px;
    background: var(--paper);
    border-bottom: 3px solid var(--gold);
  }
  .back-brand {
    position: absolute; left: 0; right: 0; top: 34px; text-align: center;
  }
  .back-brand .brand-name { font-size: 34px; }
  .back-brand .brand-rule {
    width: 250px; height: 2px; background: var(--gold); margin: 10px auto 0;
  }
  .brand-mark {
    position: absolute; left: 248px; top: 116px;
    width: 64px; height: 50px; background: var(--paper);
    border: 3px solid var(--ink);
  }
  .person {
    position: absolute; right: 298px; top: 190px; text-align: right;
    color: var(--paper);
  }
  .person-name { color: var(--gold); font-weight: 700; font-size: 22px; }
  .person-role { font-size: 13px; margin: 2px 0 10px; }
  .person-address { font-size: 12px; line-height: 1.5; }
  .divider {
    position: absolute; left: 282px; top: 190px; width: 1px; height: 100px;
    background: var(--muted); opacity: 0.6;
  }
  .contacts {
    position: absolute; left: 298px; top: 188px;
    list-style: none; color: var(--paper); font-size: 12.5px;
  }
  .contacts li { display: flex; align-items: center; gap: 9px; height: 22px; }
  .contacts svg { width: 11px; height: 11px; flex: none; }
  .contacts strong { color: var(--gold); font-weight: 700; }
</style>
</head>
<body>

<section class="card card-front" aria-label="Card front">
  <div class="front-brand">
    <div class="brand-name">HOLLOWAY<br>STONEWORKS</div>
    <div class="brand-rule"></div>
  </div>
  <p class="front-web">www.<strong>hollowaystoneworks</strong>.com.au</p>
</section>

<section class="card card-back" aria-label="Card back">
  <div class="back-top">
    <div class="back-brand">
      <div class="brand-name">HOLLOWAY STONEWORKS</div>
      <div class="brand-rule"></div>
    </div>
  </div>
  <div class="brand-mark"></div>

  <div class="person">
    <p class="person-name">Martin Brantley</p>
    <p class="person-role">Director</p>
    <p class="person-address">Suite 17, 8 Calloway Lane<br>East Penrose, Sydney NSW 2290</p>
  </div>

  <div class="divider"></div>

  <ul class="contacts">
    <li>
      <svg viewBox="0 0 12 12"><rect x="3" y="0.5" width="6" height="11" rx="1.2" fill="none" stroke="#efc12f" stroke-width="1.2"/><circle cx="6" cy="9.5" r="0.7" fill="#efc12f"/></svg>
      0431906627
    </li>
    <li>
      <svg viewBox="0 0 12 12"><path d="M2.5 1 L4.5 1 L5.3 3.6 L4 4.6 Q5.2 7 7.4 8 L8.4 6.7 L11 7.5 L11 9.5 Q10.5 11 9 11 Q1 10 1 2.5 Q1 1 2.5 1 Z" fill="#efc12f"/></svg>
      02 9634 2258
    </li>
    <li>
      <svg viewBox="0 0 12 12"><rect x="0.8" y="2.3" width="10.4" height="7.4" fill="none" stroke="#efc12f" stroke-width="1.2"/><path d="M1 2.6 L6 6.5 L11 2.6" fill="none" stroke="#efc12f" stroke-width="1.2"/></svg>
      martin@hollowaystoneworks.com.au
    </li>
    <li>
      <svg viewBox="0 0 12 12"><circle cx="6" cy="6" r="5" fill="none" stroke="#efc12f" stroke-width="1.1"/><ellipse cx="6" cy="6" rx="2.2" ry="5" fill="none" stroke="#efc12f" stroke-width="1"/><path d="M1 6 H11" stroke="#efc12f" stroke-width="1"/></svg>
      www.<strong>hollowaystoneworks</strong>.com.au
    </li>
  </ul>
</section>

</body>
</html>
```